Two Web Banners Needed for children product website! Fun and colorful!

My website is www.brightpebbletrinkets.com.au

I want 2 banners for the home page.

Size: 1920x1080px

Colors I like:
#BBA5D0
#FBF5BC
#F2BBAD

Text:
1) We create unique and meaningful gifts
2) We help you create happy memories

Fonts: provided in link

Brief:
1) I need two banners that showcase my two products on my website. I have images and fonts are included you can use in the files.
2) I want to capture child nature, friendliness and happiness.
3) I have also included samples of what I like
4) It's important to use some of the customer photographs too

Link to files:
https://filedrop-example.net/downloads/a1b2c3d4e5f60718293a4b5c6d7e8f9020220101000000/0f1e2d3c4b5a69788796a5b4c3d2e1f020220101000001/9z8y7x

If link does not work please PM me

Target Market(s)

Parents of children

Industry/Entity Type

Children ecommerce

Font styles to use
Other font styles liked:
• in file

Requirements
Must have
• Clean modern look

```html
<!DOCTYPE html>
<html lang="en">
<head>
<meta charset="UTF-8">
<title>Unique and Meaningful Gifts – Banner</title>
<link rel="stylesheet" href="https://fonts.googleapis.com/css2?family=Open+Sans:wght@600;700;800&family=Mrs+Saint+Delafield&display=swap">
<style>
  :root {
    --peach: #f2bbad;
    --peach-deep: #efb1a1;
    --butter: #fbf5bc;
    --lavender: #bba5d0;
    --lavender-soft: #d9cce6;
    --ink: #0c0c0c;
    --white: #ffffff;
  }
  * { margin: 0; padding: 0; box-sizing: border-box; }
  html, body { width: 1200px; height: 675px; overflow: hidden; background: var(--white); }
  .banner {
    position: relative;
    width: 1200px;
    height: 675px;
    overflow: hidden;
    background: var(--white);
    font-family: "Open Sans", Arial, sans-serif;
  }
  .backdrop, .decor { position: absolute; inset: 0; width: 1200px; height: 675px; }
  .tagline-script {
    position: absolute;
    left: 94px;
    top: 92px;
    font-family: "Mrs Saint Delafield", cursive;
    font-size: 82px;
    line-height: 1;
    color: var(--ink);
    white-space: nowrap;
  }
  .headline {
    position: absolute;
    left: 88px;
    top: 180px;
    font-weight: 600;
    font-size: 86px;
    line-height: 84px;
    color: var(--ink);
    letter-spacing: -0.5px;
  }
  .headline .accent { color: var(--peach); }
  .headline span { display: block; }
  .cta {
    position: absolute;
    left: 84px;
    top: 484px;
    width: 267px;
    height: 70px;
    border-radius: 22px;
    background: var(--peach);
    color: var(--white);
    font-weight: 800;
    font-size: 41px;
    letter-spacing: -0.5px;
    display: flex;
    align-items: center;
    justify-content: center;
    text-decoration: none;
  }
  .photo-group {
    position: absolute;
    left: 600px;
    top: 100px;
    width: 598px;
    height: 545px;
    border-radius: 46% 40% 30% 36% / 34% 34% 26% 28%;
    background: linear-gradient(160deg, #c9c3b8 0%, #8e95ae 35%, #2f3f8f 62%, #d8d3a3 100%);
    opacity: 0.85;
  }
  .bird {
    position: absolute;
    width: 52px;
    height: 48px;
    border-radius: 50% 45% 50% 40%;
    background: var(--lavender-soft);
  }
  .bird--top { left: 23px; top: 110px; }
  .bird--bottom { left: 305px; top: 568px; }
  .bottle {
    position: absolute;
    left: 1085px;
    top: 168px;
    width: 44px;
    height: 40px;
    border-radius: 10px;
    background: #f7d8cf;
    transform: rotate(-40deg);
  }
</style>
</head>
<body>
<main class="banner">
  <svg class="backdrop" viewBox="0 0 1200 675" aria-hidden="true">
    <path d="M650 205 C700 150 800 160 860 195 C930 235 1020 230 1100 215 C1170 205 1200 230 1200 260 L1200 675 L472 675 C500 600 540 560 545 490 C550 420 520 380 560 330 C590 290 620 245 650 205 Z" fill="var(--peach)"/>
    <path d="M478 520 C520 450 600 430 640 480 C690 540 650 620 700 675 L478 675 C455 620 455 560 478 520 Z" fill="var(--butter)"/>
    <path d="M1090 430 C1140 400 1200 410 1200 410 L1200 560 C1160 560 1110 530 1090 500 Z" fill="var(--butter)"/>
    <path d="M820 640 C860 620 900 640 910 675 L820 675 Z" fill="var(--butter)"/>
  </svg>

  <svg class="decor" viewBox="0 0 1200 675" aria-hidden="true">
    <!-- paper plane -->
    <path d="M318 58 L358 88 L338 92 L318 110 Z M338 92 L318 58" fill="none" stroke="var(--peach)" stroke-width="2" stroke-linejoin="round"/>
    <g fill="var(--peach)"><circle cx="347" cy="116" r="1.8"/><circle cx="342" cy="128" r="1.8"/><circle cx="336" cy="139" r="1.8"/><circle cx="331" cy="150" r="1.8"/></g>
    <!-- sparkle strokes -->
    <g stroke="var(--peach)" stroke-width="2" fill="none" stroke-linecap="round">
      <path d="M650 128 L673 145"/><path d="M668 115 L681 135"/><path d="M692 106 L690 128"/>
      <path d="M795 66 C800 76 808 82 820 84"/><path d="M803 76 C808 82 813 86 822 88"/>
      <path d="M975 58 C970 68 964 76 960 82"/><path d="M987 74 C982 80 977 85 972 88"/>
    </g>
    <!-- stars -->
    <path d="M1136 18 L1142 30 L1155 30 L1145 38 L1149 51 L1136 43 L1124 51 L1128 38 L1118 30 L1131 30 Z" fill="var(--lavender-soft)"/>
    <path d="M460 438 L465 448 L476 448 L468 455 L471 466 L460 460 L450 466 L453 455 L445 448 L456 448 Z" fill="#f5c8bb"/>
    <!-- hearts -->
    <path d="M318 428 C296 412 284 398 289 384 C294 372 310 372 318 383 C326 372 344 370 348 384 C352 398 340 412 318 428 Z" fill="var(--peach)"/>
    <path d="M44 648 C32 640 26 632 29 625 C32 619 40 619 44 625 C48 619 57 619 60 625 C62 632 56 640 44 648 Z" fill="var(--lavender-soft)"/>
  </svg>

  <div class="bird bird--top" role="img" aria-label="Small lavender bird doodle"></div>
  <div class="bird bird--bottom" role="img" aria-label="Small lavender bird doodle"></div>
  <div class="bottle" role="img" aria-label="Baby bottle doodle"></div>

  <div class="photo-group" role="img" aria-label="Photo of smiling toddlers playing around a small white table with personalised upholstered kids chairs embroidered with their names"></div>

  <p class="tagline-script">We create</p>
  <h1 class="headline">
    <span><em class="accent" style="font-style:normal">Unique</em> and</span>
    <span>Meaningful</span>
    <span>Gifts</span>
  </h1>
  <a class="cta" href="#shop">SHOP NOW</a>
</main>
</body>
</html>
```